Verdanix Medical Business Card

Create a high class Business card for Medical Aesthetics and Wellness Practice called Verdanix Medical Aesthetics and Wellness as per the logo attached.
Addresss is: 418 Harlan Brook Road Suite 312 Ashbrook, New York 11093
Phone (555)204-7391 IG @verdanix_medical
Verdanixmedical.example

I need 5 different name configurations
1) Dr. Theo Valcourt
Aesthetics and Wellness Specialist
Medical Director

2) Rosalind Pettinger, NP
Clinical Nurse Manager

3) Marla Vostrik, RN
Aesthetic Nurse Specialist

4) Petra Halvesen, RN

5) Dana Kowbeck, L.E.
Senior Licensed Esthetician

Target Market(s)

22-55 Females

Industry/Entity Type

Medical Spa and Wellness

Contact Information for Business Card

Logo, address, phone, web, instagram, providers name

Requirements
Must have
• Attractive classy modern look

```html
<!DOCTYPE html>
<html lang="en">
<head>
<meta charset="utf-8">
<title>Verdanix Medical Business Card</title>
<link rel="stylesheet" href="https://fonts.googleapis.com/css2?family=Cormorant+Garamond:wght@400;500&family=Libre+Franklin:wght@300;400&display=swap">
<style>
  :root {
    --bg: #969696;
    --teal: #144f60;
    --ink: #1a4557;
    --paper: #ffffff;
    --muted: #7a7a7a;
    --white: #ffffff;
  }
  * { margin: 0; padding: 0; box-sizing: border-box; }
  html, body { width: 1200px; height: 1000px; overflow: hidden; background: var(--bg); }
  .canvas { position: relative; width: 1200px; height: 1000px; }
  .card { position: absolute; width: 694px; height: 400px; border-radius: 18px; }
  .card-front { left: 258px; top: 68px; background: var(--teal); }
  .card-back { left: 253px; top: 525px; background: var(--paper); }

  .brand { position: absolute; text-align: center; font-family: "Cormorant Garamond", serif; font-weight: 400; }
  .brand-name { display: block; letter-spacing: 4px; line-height: 1; }
  .brand-tagline { display: block; text-transform: uppercase; letter-spacing: 0.5px; }
  .brand-city { display: block; text-transform: uppercase; }

  .card-front .brand { left: 62px; width: 370px; top: 158px; color: var(--white); }
  .card-front .brand-name { font-size: 58px; }
  .card-front .brand-tagline { font-size: 18px; margin-top: 14px; }
  .card-front .brand-city { font-size: 11px; letter-spacing: 6px; margin-top: 10px; }

  .card-back .brand { left: 52px; width: 256px; top: 185px; color: var(--ink); }
  .card-back .brand-name { font-size: 42px; }
  .card-back .brand-tagline { font-size: 12.5px; margin-top: 9px; }
  .card-back .brand-city { font-size: 8px; letter-spacing: 4.5px; margin-top: 6px; }

  .provider { position: absolute; left: 364px; top: 124px; color: var(--ink); }
  .provider-name { font-family: "Cormorant Garamond", serif; font-weight: 500; font-size: 25px; letter-spacing: 0.8px; text-transform: uppercase; line-height: 1; }
  .provider-role { font-family: "Libre Franklin", sans-serif; font-weight: 400; font-size: 14.5px; line-height: 16px; letter-spacing: 0.3px; margin-top: 4px; }

  .contacts { position: absolute; left: 364px; top: 203px; list-style: none; font-family: "Libre Franklin", sans-serif; font-weight: 300; font-size: 16.5px; color: var(--muted); }
  .contacts li { display: flex; align-items: center; height: 21px; }
  .contacts svg { width: 16px; height: 16px; margin-right: 7px; flex: none; }

  .address { position: absolute; left: 364px; top: 294px; font-family: "Libre Franklin", sans-serif; font-weight: 300; font-size: 15px; line-height: 19px; color: var(--muted); font-style: normal; }
</style>
</head>
<body>
<main class="canvas">
  <section class="card card-front">
    <div class="brand">
      <span class="brand-name">verdanix</span>
      <span class="brand-tagline">Medical Aesthetics and Wellness</span>
      <span class="brand-city">New York</span>
    </div>
  </section>

  <section class="card card-back">
    <div class="brand">
      <span class="brand-name">verdanix</span>
      <span class="brand-tagline">Medical Aesthetics and Wellness</span>
      <span class="brand-city">New York</span>
    </div>

    <div class="provider">
      <h1 class="provider-name">Dr. Theo Valcourt</h1>
      <p class="provider-role">Aesthetics and Wellness Specialist<br>Medical Director</p>
    </div>

    <ul class="contacts">
      <li>
        <svg viewBox="0 0 16 16" aria-hidden="true"><path fill="#1a4557" d="M3.2 1.5l2.3-.3 1.4 3.3-1.5 1.2c.8 1.7 2.2 3.1 3.9 3.9l1.2-1.5 3.3 1.4-.3 2.3c-.1.8-.8 1.4-1.6 1.3C6.6 12.7 2.2 8.3 1.9 3.1c0-.8.5-1.5 1.3-1.6z"/></svg>
        (555) 204-7391
      </li>
      <li>
        <svg viewBox="0 0 16 16" aria-hidden="true"><circle cx="8" cy="8" r="6.3" fill="none" stroke="#1a4557" stroke-width="1.8"/></svg>
        @verdanix_medical
      </li>
      <li>
        <svg viewBox="0 0 16 16" aria-hidden="true" fill="none" stroke="#1a4557" stroke-width="1.3"><circle cx="8" cy="8" r="6.6"/><ellipse cx="8" cy="8" rx="2.8" ry="6.6"/><path d="M1.4 8h13.2M2.4 4.6h11.2M2.4 11.4h11.2"/></svg>
        verdanixmedical.example
      </li>
    </ul>

    <address class="address">418 Harlan Brook Road Suite 312<br>Ashbrook, New York 11093</address>
  </section>
</main>
</body>
</html>
```